Quorvel Marketing & Design needs a Wordpress website

We need a wordpress design for a new marketing and design company in Australia called 'Quorvel Marketing & Design". The website needs to be responsive, modern, and attract new customers. It needs to be unique and different. We provide marketing and design solutions for small businesses from consulting, to flyer distribution to Facebook ads etc. We would like to see designs that use the Quorvel logo colours. The final design should communicate professionalism, creativity & growth. It needs to stand out from the crowd.

Target Market(s)

Small Business who need a marketing freelancer to help them grow

Industry/Entity Type

Marketing

Number of Pages Required

3 page

Requirements
Must have
• Home page, services page & contact page

```html
<!DOCTYPE html>
<html lang="en">
<head>
<meta charset="utf-8">
<title>Quorvel Marketing &amp; Design</title>
<link rel="stylesheet" href="https://fonts.googleapis.com/css2?family=Oswald:wght@400;500;600&family=Open+Sans:wght@400;600;700&display=swap">
<style>
  :root {
    --pink: #e4157e;
    --pink-deep: #b80f66;
    --pink-soft: #f07ab5;
    --navy: #2b2350;
    --ink: #1f1f24;
    --text: #4a4a52;
    --white: #ffffff;
    --paper: #e9e9ec;
    --footer: #1b1b1d;
    --footer-line: #3a3a3e;
  }
  * { box-sizing: border-box; margin: 0; padding: 0; }
  html, body { width: 1200px; height: 2628px; overflow: hidden; }
  body { font-family: "Open Sans", Arial, sans-serif; color: var(--text); background: var(--white); }

  /* Hero */
  .hero { position: relative; height: 640px; overflow: hidden; }
  .hero-photo { position: absolute; inset: 0;
    background: linear-gradient(120deg, #f4f4f6 0%, #d9d9de 45%, #ecebef 70%, #cfc9c0 100%); }
  .hero-content { position: relative; text-align: center; padding-top: 56px; }
  .hero-mark { width: 108px; height: 108px; border-radius: 50%; background: var(--pink);
    margin: 0 auto; border: 6px solid var(--white); box-shadow: 0 4px 14px rgba(0,0,0,.15); }
  .hero-title { font-family: "Oswald", Arial, sans-serif; font-weight: 500; color: var(--ink);
    font-size: 56px; line-height: 64px; letter-spacing: 2px; margin-top: 86px; text-transform: uppercase; }
  .hero-sub { font-size: 17px; color: var(--ink); margin-top: 14px; display: inline-block;
    border-bottom: 2px solid var(--pink); padding-bottom: 12px; }
  .hero-down { display: block; margin: 26px auto 0; }

  /* Nav */
  .site-nav { height: 108px; display: flex; align-items: center; justify-content: space-between;
    padding: 0 60px 0 70px; border-bottom: 1px solid #e3e3e6; background: var(--white); }
  .brand { display: flex; align-items: center; gap: 14px; }
  .brand-dot { width: 64px; height: 64px; border-radius: 50%; background: var(--pink); }
  .brand-name { font-family: "Oswald", Arial, sans-serif; font-weight: 600; font-size: 40px; color: var(--ink); line-height: 1; }
  .brand-tag { font-size: 13px; font-weight: 600; color: var(--pink); letter-spacing: 1px; text-transform: uppercase; margin-top: 4px; }
  .menu { display: flex; list-style: none; height: 108px; }
  .menu li { font-size: 19px; font-weight: 600; color: var(--ink); padding: 0 32px;
    display: flex; align-items: center; border-left: 1px solid #e3e3e6; }
  .menu li.active { color: var(--pink); }

  /* Welcome */
  .welcome { text-align: center; padding: 60px 180px 0; height: 1140px - 748px; }
  .welcome h1 { font-family: "Oswald", Arial, sans-serif; font-weight: 600; font-size: 52px; color: var(--ink); letter-spacing: 2px; }
  .welcome h2 { font-family: "Oswald", Arial, sans-serif; font-weight: 400; font-size: 48px; color: var(--pink); letter-spacing: 1px; margin-top: -2px; }
  .welcome p { font-size: 16px; line-height: 26px; color: var(--text); margin-top: 28px; }

  /* Services */
  .services { position: absolute; top: 1140px; left: 0; width: 1200px; height: 620px; text-align: center; color: var(--white); }
  .services-photo { position: absolute; inset: 0;
    background: linear-gradient(135deg, #f05fa8 0%, #e4157e 45%, #c81273 75%, #a90f62 100%); }
  .services-inner { position: relative; padding-top: 44px; }
  .section-title { font-family: "Oswald", Arial, sans-serif; font-weight: 500; font-size: 54px; letter-spacing: 2px; text-transform: uppercase; }
  .services .section-title::after { content: ""; display: block; width: 120px; height: 3px; background: var(--white); margin: 10px auto 0; }
  .service-list { display: flex; justify-content: center; gap: 50px; margin-top: 56px; }
  .service { width: 210px; }
  .service-icon { width: 128px; height: 128px; border-radius: 50%; background: var(--pink); border: 6px solid var(--white);
    margin: 0 auto; }
  .service h3 { font-size: 26px; font-weight: 400; margin-top: 28px; }
  .service p { font-size: 14px; line-height: 20px; margin-top: 10px; color: #fde3f0; }
  .btn { display: inline-block; background: var(--navy); color: var(--white); font-size: 18px; font-weight: 600;
    padding: 10px 22px; margin-top: 22px; text-transform: uppercase; }

  /* Testimonial */
  .testimonial { position: absolute; top: 1800px; left: 0; width: 1200px; text-align: center; }
  .testimonial .section-title { color: var(--ink); font-size: 50px; }
  .testimonial .section-title span { color: var(--pink); }
  .quote-mark { font-family: "Oswald", Arial, sans-serif; font-size: 70px; color: #999; line-height: 40px; margin-top: 16px; }
  .avatar { width: 120px; height: 120px; border-radius: 50%; background: linear-gradient(160deg, #d8c7b8, #8f7a6c);
    border: 4px solid #ddd; margin: 18px auto 0; }
  .testimonial p { font-size: 16px; line-height: 26px; padding: 0 190px; margin-top: 34px; }
  .client-name { color: var(--pink); font-weight: 700; font-size: 15px; margin-top: 20px; }
  .dots { display: flex; justify-content: center; gap: 16px; margin-top: 18px; }
  .dots i { width: 16px; height: 16px; border-radius: 50%; background: var(--ink); display: block; }
  .dots i.on { background: var(--pink); }

  /* Footer */
  .site-footer { position: absolute; top: 2272px; left: 0; width: 1200px; height: 356px;
    background: repeating-linear-gradient(90deg, #1e1e20 0 6px, #18181a 6px 12px); color: var(--white); text-align: center; }
  .footer-menu { display: flex; justify-content: center; gap: 60px; list-style: none; padding-top: 48px; font-size: 17px; }
  .call { display: flex; justify-content: center; align-items: center; gap: 26px; margin-top: 52px;
    font-family: "Oswald", Arial, sans-serif; font-size: 44px; letter-spacing: 1px; }
  .social { display: flex; justify-content: center; gap: 26px; margin-top: 40px; }
  .social i { width: 52px; height: 52px; border-radius: 50%; background: var(--pink); display: block; }
  .copyright { font-size: 14px; color: #ccc; margin-top: 34px; }
  .copyright span { color: var(--pink); }
</style>
</head>
<body>

<header class="hero">
  <div class="hero-photo" role="img" aria-label="Photo of a curled sheet of paper and coloured pencils on a light desk"></div>
  <div class="hero-content">
    <div class="hero-mark" role="img" aria-label="Quorvel mark"></div>
    <div class="hero-title">We<br>Love Design &amp;<br>Marketing</div>
    <div class="hero-sub">Lorem Ipsum is simply dummy text of the print</div>
    <svg class="hero-down" width="64" height="64" viewBox="0 0 64 64" aria-hidden="true">
      <circle cx="32" cy="32" r="29" fill="none" stroke="#e4157e" stroke-width="3"/>
      <path d="M32 18 V44 M22 34 L32 44 L42 34" fill="none" stroke="#e4157e" stroke-width="3" stroke-linecap="round" stroke-linejoin="round"/>
    </svg>
  </div>
</header>

<nav class="site-nav">
  <div class="brand">
    <span class="brand-dot"></span>
    <div>
      <div class="brand-name">Quorvel</div>
      <div class="brand-tag">Marketing &amp; Design</div>
    </div>
  </div>
  <ul class="menu">
    <li class="active">HOME</li>
    <li>ABOUT</li>
    <li>SERVICES</li>
    <li>CLIENTS</li>
    <li>CONTACT</li>
  </ul>
</nav>

<section class="welcome">
  <h1>WELCOME</h1>
  <h2>QUORVEL MARKETING &amp; DESIGN</h2>
  <p>Lorem Ipsum is simply dummy text of the printing and typesetting industry. Lorem Ipsum has been the industry's standard dummy text ever since the 1500s, when an unknown printer took a galley of type and scrambled it to make a type specimen book.</p>
  <p>Lorem Ipsum is simply dummy text of the printing and typesetting industry. Lorem Ipsum has been the industry's standard dummy text ever since the 1500.</p>
</section>

<section class="services">
  <div class="services-photo" role="img" aria-label="Pink-toned photo of a person working at a desk with a pen"></div>
  <div class="services-inner">
    <h2 class="section-title">Our Services</h2>
    <div class="service-list">
      <div class="service">
        <div class="service-icon" role="img" aria-label="Logo design icon"></div>
        <h3>LOGO DESIGN</h3>
        <p>Lorem Ipsum is simply dummy text of the printing and typesetting industry.</p>
        <span class="btn">Read More</span>
      </div>
      <div class="service">
        <div class="service-icon" role="img" aria-label="Corporate identity icon"></div>
        <h3>Corporate Identity</h3>
        <p>Lorem Ipsum is simply dummy text of the printing and typesetting industry.</p>
        <span class="btn">Read More</span>
      </div>
      <div class="service">
        <div class="service-icon" role="img" aria-label="Flyers icon"></div>
        <h3>Flyers</h3>
        <p>Lorem Ipsum is simply dummy text of the printing and typesetting industry.</p>
        <span class="btn">Read More</span>
      </div>
      <div class="service">
        <div class="service-icon" role="img" aria-label="Consulting icon"></div>
        <h3>Consulting</h3>
        <p>Lorem Ipsum is simply dummy text of the printing and typesetting industry.</p>
        <span class="btn">Read More</span>
      </div>
    </div>
  </div>
</section>

<section class="testimonial">
  <h2 class="section-title">Our Client <span>Love Us</span></h2>
  <div class="quote-mark">&ldquo;</div>
  <div class="avatar" role="img" aria-label="Client portrait photo"></div>
  <p>Lorem Ipsum is simply dummy text of the printing and typesetting industry. Lorem Ipsum has been the industry's standard dummy text ever since the 1500s, when an unknown printer took a galley of type and scrambled it to make a type specimen book.</p>
  <div class="client-name">- Client Name</div>
  <div class="dots"><i class="on"></i><i></i><i></i><i></i></div>
</section>

<footer class="site-footer">
  <ul class="footer-menu">
    <li>HOME</li><li>ABOUT</li><li>SERVICES</li><li>CLIENTS</li><li>CONTACT</li>
  </ul>
  <div class="call">
    <span>CALL US ON</span>
    <svg width="44" height="44" viewBox="0 0 24 24" aria-hidden="true">
      <path fill="#e4157e" d="M6.6 10.8a15.1 15.1 0 0 0 6.6 6.6l2.2-2.2a1 1 0 0 1 1-.25 11.4 11.4 0 0 0 3.6.57 1 1 0 0 1 1 1V20a1 1 0 0 1-1 1A17 17 0 0 1 3 4a1 1 0 0 1 1-1h3.5a1 1 0 0 1 1 1c0 1.25.2 2.45.57 3.6a1 1 0 0 1-.25 1z"/>
    </svg>
    <span>1234567890</span>
  </div>
  <div class="social">
    <i role="img" aria-label="Social profile"></i>
    <i role="img" aria-label="Social profile"></i>
    <i role="img" aria-label="Social profile"></i>
    <i role="img" aria-label="Social profile"></i>
  </div>
  <div class="copyright">&copy; <span>Quorvel Marketing &amp; Design</span> - 2015, All Rights Reserved &nbsp;|&nbsp; <span>Terms &amp; Condition</span></div>
</footer>

</body>
</html>
```